Business cards / Letterheads / Compliment slips

We are looking to get business cards, letterheads and compliment slips designed.

These will all have to follow the design of our new website and logo. Links to the website, logo and fonts can be found below...

The designs need to be simple with focus on the typography. Only the following colours should be used on the designs...

#7f9d3c
#191818
#fff

Website:
http://brookfieldweb.examplestudio.co.uk/

Logo:
https://www.filecrate.example/sh/8kd2m4qwzpla7ve/hTr5NpQ2Xw/logos

Fonts:
https://www.filecrate.example/sh/8kd2m4qwzpla7ve/Q9vTzR3mKe/Fonts/BayerModern_TTF

and

https://www.filecrate.example/sh/8kd2m4qwzpla7ve/W7nHcY5pD3/Fonts/MuseoSansFamily

Reason: We would like some more design submissions

Reason: We are still deciding on designs we like and would like to see some more submissions...

Industry/Entity Type

Business

Requirements
Must have
• The designs need to be simple with focus on the typography. Only the following colours should be used on the designs...

#7f9d3c
#191818
#fff
Should not have
• - Any fonts that are not provided.
- Any colours that are not provided.

```html
<!DOCTYPE html>
<html lang="en">
<head>
<meta charset="utf-8">
<title>Brookfield Web – Business Card</title>
<link rel="stylesheet" href="https://fonts.googleapis.com/css2?family=Mulish:wght@300;400;800&display=swap">
<style>
  :root {
    --brand-green: #7f9d3c;
    --brand-ink: #191818;
    --brand-white: #fff;
    --backdrop: #dde3e6;
    --divider: #d6d6d6;
  }
  html, body {
    margin: 0;
    padding: 0;
    width: 1200px;
    height: 960px;
    overflow: hidden;
    background: var(--backdrop);
    font-family: "Mulish", sans-serif;
  }
  .sheet {
    position: relative;
    width: 1200px;
    height: 960px;
  }
  .card {
    position: absolute;
    left: 250px;
    width: 700px;
    height: 400px;
    box-shadow: 0 6px 18px rgba(0, 0, 0, 0.18);
  }
  .card--front {
    top: 60px;
    background: var(--brand-white);
  }
  .card--back {
    top: 500px;
    background: var(--brand-ink);
  }

  .contact-column {
    position: absolute;
    bottom: 48px;
    writing-mode: vertical-rl;
    transform: rotate(180deg);
    font-size: 19px;
    font-weight: 400;
    line-height: 1.3;
    color: var(--brand-ink);
    white-space: nowrap;
  }
  .contact-column--phone {
    left: 62px;
    color: var(--brand-green);
    font-size: 22px;
  }
  .contact-column--email { left: 126px; }
  .contact-column--web { left: 184px; }
  .contact-column--address { left: 240px; }

  .card-divider {
    position: absolute;
    left: 340px;
    top: 44px;
    bottom: 44px;
    width: 1px;
    background: var(--divider);
  }

  .holder {
    position: absolute;
    left: 380px;
    top: 118px;
    color: var(--brand-green);
  }
  .holder-name {
    margin: 0;
    font-size: 42px;
    font-weight: 300;
    line-height: 1.18;
    letter-spacing: 1px;
    text-transform: uppercase;
  }
  .holder-role {
    margin: 10px 0 0 4px;
    font-size: 21px;
    font-weight: 400;
  }

  .brand-lockup {
    position: absolute;
    inset: 0;
    display: flex;
    align-items: center;
    justify-content: center;
    gap: 22px;
  }
  .brand-dot {
    width: 82px;
    height: 82px;
  }
  .brand-name {
    font-size: 62px;
    font-weight: 800;
    color: var(--brand-white);
    letter-spacing: -1px;
  }
</style>
</head>
<body>
<main class="sheet">
  <section class="card card--front" aria-label="Business card front">
    <div class="contact-column contact-column--phone">0854 310 4827</div>
    <div class="contact-column contact-column--email">hello@brookfieldweb.co.uk</div>
    <div class="contact-column contact-column--web">brookfieldweb.examplestudio.co.uk</div>
    <div class="contact-column contact-column--address">Suite 7, 22 Orchard Lane,<br>Ashbury , AB9 4XZ</div>
    <div class="card-divider"></div>
    <div class="holder">
      <h1 class="holder-name">Helena<br>Marsh</h1>
      <p class="holder-role">Manager</p>
    </div>
  </section>

  <section class="card card--back" aria-label="Business card back">
    <div class="brand-lockup">
      <svg class="brand-dot" viewBox="0 0 82 82" aria-hidden="true">
        <circle cx="41" cy="41" r="41" fill="var(--brand-green)"/>
      </svg>
      <span class="brand-name">brookfieldweb</span>
    </div>
  </section>
</main>
</body>
</html>
```